Business Card Design for Small Electrical Contractor

I need to update my business card into something a little more modern. We are a small electrical contracting company. We service domestic and commercial places around Sydney. We have 2 logo designs at the moment. I have uploaded both and 2 different sizes to work with.

Industry/Entity Type

Business

Contact Information for Business Card

Leo Hartigan
8/21-23 Birch Rd, Kelsworth 2087
t - (02) 9381 4720
m - 0427 815 903
E - info@hartiganelx.com.au
W - hartiganelx.com.au
ABN: 42 907 551 316

Font styles to use
Sans Serif

Requirements
Must have
• I would also like to see the below fit on somewhere aswell
• - Licensed Electrician
• - Level 2 (Cat 1 & 4)
• - Domestic
• - Commercial
• - Repairs and Installations
• - Data
Nice to have
• Try and keep similar colours as logo
Should not have
• No lightning bolts or light globes. Smart and professional please.

```html
<!DOCTYPE html>
<html lang="en">
<head>
<meta charset="utf-8">
<title>Hartigan Electrical – Business Card</title>
<link href="https://fonts.googleapis.com/css2?family=Oswald:wght@500;700&family=Roboto:wght@300;400;500&display=swap" rel="stylesheet">
<style>
  :root {
    --ink: #1f2a2a;
    --amber: #f0a01c;
    --paper: #ffffff;
    --backdrop: #e8e5e0;
    --icon-dark: #0d1414;
  }
  * { box-sizing: border-box; margin: 0; padding: 0; }
  html, body { width: 1200px; height: 1009px; overflow: hidden; }
  body {
    background: var(--backdrop);
    font-family: "Roboto", Arial, sans-serif;
    position: relative;
  }
  .card {
    position: absolute;
    left: 220px;
    width: 760px;
    height: 440px;
    background: var(--paper);
    box-shadow: 0 10px 28px rgba(0,0,0,.18);
    overflow: hidden;
  }
  .card--front { top: 40px; }
  .card--back { top: 529px; }

  .brand {
    position: absolute;
    color: var(--ink);
    font-family: "Roboto", Arial, sans-serif;
    font-weight: 500;
    letter-spacing: .04em;
    white-space: nowrap;
    display: flex;
    align-items: center;
    gap: 12px;
    line-height: 1.15;
  }
  .brand__mark {
    width: 14px; height: 14px;
    flex: none;
    background: var(--amber);
  }
  .card--front .brand { left: 40px; top: 184px; font-size: 25px; }
  .card--back .brand { left: 0; right: 0; top: 96px; justify-content: center; font-size: 44px; }

  .abn {
    position: absolute;
    top: 34px; right: 40px;
    font-size: 14px;
    color: var(--ink);
    font-weight: 400;
  }

  .contact-panel {
    position: absolute;
    left: 290px; right: 0;
    top: 130px; bottom: 40px;
    background: var(--ink);
    border: 7px solid var(--amber);
    border-right: none;
  }
  .name-plate {
    position: absolute;
    left: 14px; top: 58px;
    width: 184px; height: 150px;
    background: var(--amber);
    border-radius: 4px;
    display: flex;
    flex-direction: column;
    justify-content: center;
    align-items: center;
    color: var(--ink);
    text-align: center;
  }
  .name-plate__name {
    font-family: "Oswald", Arial, sans-serif;
    font-weight: 700;
    font-size: 27px;
    line-height: 1;
    text-transform: uppercase;
    white-space: nowrap;
  }
  .name-plate__role {
    font-family: "Oswald", Arial, sans-serif;
    font-weight: 500;
    font-size: 15px;
    margin-top: 6px;
    text-transform: uppercase;
  }
  .contact-list {
    position: absolute;
    left: 216px; top: 34px;
    list-style: none;
    color: #fff;
    font-size: 13px;
    font-weight: 300;
    line-height: 1.45;
    white-space: nowrap;
  }
  .contact-list li {
    display: flex;
    align-items: center;
    gap: 12px;
    margin-bottom: 18px;
  }
  .icon {
    width: 32px; height: 32px;
    flex: none;
    border-radius: 6px;
    display: flex; align-items: center; justify-content: center;
  }
  .icon--dark { background: var(--icon-dark); }
  .icon--amber { background: var(--amber); }

  .rule {
    position: absolute;
    left: 230px; right: 230px;
    top: 166px;
    height: 2px;
    background: var(--amber);
  }
  .services {
    position: absolute;
    left: 0; right: 0; bottom: 0;
    height: 170px;
    background: var(--ink);
    display: grid;
    grid-template-columns: repeat(3, 1fr);
    grid-template-rows: repeat(2, 1fr);
    padding: 26px 50px;
    list-style: none;
    color: #fff;
    font-size: 15px;
    font-weight: 300;
  }
  .services li { display: flex; align-items: center; gap: 12px; white-space: nowrap; }
  .services .icon { width: 30px; height: 30px; }
</style>
</head>
<body>

<section class="card card--front" aria-label="Business card front">
  <div class="brand"><span class="brand__mark"></span><span>Hartigan<br>Electrical</span></div>
  <p class="abn">ABN: 42 907 551 316</p>

  <div class="contact-panel">
    <div class="name-plate">
      <p class="name-plate__name">Leo Hartigan</p>
      <p class="name-plate__role">General Manager</p>
    </div>
    <ul class="contact-list">
      <li>
        <span class="icon icon--dark">
          <svg width="18" height="18" viewBox="0 0 24 24"><path fill="#fff" d="M6.6 10.8a15.1 15.1 0 0 0 6.6 6.6l2.2-2.2c.3-.3.7-.4 1-.2 1.1.4 2.3.6 3.6.6.6 0 1 .4 1 1V20c0 .6-.4 1-1 1A17 17 0 0 1 3 4c0-.6.4-1 1-1h3.5c.6 0 1 .4 1 1 0 1.3.2 2.5.6 3.6.1.3 0 .7-.2 1z"/></svg>
        </span>
        <span>(02) 9381 4720<br>0427 815 903</span>
      </li>
      <li>
        <span class="icon icon--amber">
          <svg width="18" height="18" viewBox="0 0 24 24" fill="none" stroke="#1f2a2a" stroke-width="2"><circle cx="12" cy="12" r="9"/><path d="M3 12h18M12 3c3 3 3 15 0 18M12 3c-3 3-3 15 0 18"/></svg>
        </span>
        <span>info@hartiganelx.com.au<br>www.hartiganelx.com.au</span>
      </li>
      <li>
        <span class="icon icon--dark">
          <svg width="18" height="18" viewBox="0 0 24 24"><path fill="#fff" d="M12 2a7 7 0 0 0-7 7c0 5 7 13 7 13s7-8 7-13a7 7 0 0 0-7-7zm0 9.5A2.5 2.5 0 1 1 12 6.5a2.5 2.5 0 0 1 0 5z"/></svg>
        </span>
        <span>8/21-23 Birch Rd, Kelsworth<br>2087</span>
      </li>
    </ul>
  </div>
</section>

<section class="card card--back" aria-label="Business card back">
  <div class="brand"><span class="brand__mark"></span>Hartigan Electrical</div>
  <div class="rule"></div>
  <ul class="services">
    <li><span class="icon icon--amber"><svg width="16" height="16" viewBox="0 0 24 24" fill="none" stroke="#1f2a2a" stroke-width="3"><path d="M4 12l5 5L20 6"/></svg></span>Licensed Electrician</li>
    <li><span class="icon icon--amber"><svg width="16" height="16" viewBox="0 0 24 24" fill="none" stroke="#1f2a2a" stroke-width="3"><path d="M4 12l5 5L20 6"/></svg></span>Level 2 (Cat 1 &amp; 4)</li>
    <li><span class="icon icon--amber"><svg width="16" height="16" viewBox="0 0 24 24" fill="none" stroke="#1f2a2a" stroke-width="3"><path d="M4 12l5 5L20 6"/></svg></span>Domestic</li>
    <li><span class="icon icon--amber"><svg width="16" height="16" viewBox="0 0 24 24" fill="none" stroke="#1f2a2a" stroke-width="3"><path d="M4 12l5 5L20 6"/></svg></span>Commercial</li>
    <li><span class="icon icon--amber"><svg width="16" height="16" viewBox="0 0 24 24" fill="none" stroke="#1f2a2a" stroke-width="3"><path d="M4 12l5 5L20 6"/></svg></span>Repairs and Installations</li>
    <li><span class="icon icon--amber"><svg width="16" height="16" viewBox="0 0 24 24" fill="none" stroke="#1f2a2a" stroke-width="3"><path d="M4 12l5 5L20 6"/></svg></span>Data</li>
  </ul>
</section>

</body>
</html>
```